Whitcombe Framing Works - Card Design

I am looking to use the logo designs that you already did for me to develop a business card. I would like the card to have a black background and be double sided. I want white and green logo and text. I have attached an inspiration photo of a look that I like. I would like to use the Vertical Logo attached to take up the full front side of the card. On the back where I have my name and information, I would like to have the horizontal logo or maybe even just the image of the 'A' and trees without the text. I am open, but I am looking for something clean and simple and I want the green to really pop! Additional files can be found under Design #: 40593216

Target Market(s)

Homeowners

Industry/Entity Type

Construction

Contact Information for Business Card

Name: Marcus Pellow, Title: Project Manager, Phone: 831.555.0147, Email: whitcombeframingworks@mailbarn.net, address: 418 Juniper Ln, Felton, CA 95092, Lic# 2046318

Colors
00AB8E
00BBA5
67D7C9
C6EFE9
E9F9F6

Requirements
Nice to have
• I would like to see the logos that I have already got from SketchHarbor, though I am open to new ones

```html
<!DOCTYPE html>
<html lang="en">
<head>
<meta charset="utf-8">
<title>Whitcombe Framing Works – Business Card</title>
<link rel="stylesheet" href="https://fonts.googleapis.com/css2?family=Montserrat:wght@400;500;600;700&display=swap">
<style>
  :root {
    --backdrop: #d9d4cc;
    --card: #262626;
    --card-edge: #1c1c1c;
    --green: #6cbf4a;
    --white: #ffffff;
    --soft-white: #e6e6e6;
  }
  * { box-sizing: border-box; margin: 0; padding: 0; }
  html, body {
    width: 900px; height: 1200px; overflow: hidden;
    background: var(--backdrop);
    font-family: "Montserrat", sans-serif;
  }
  .canvas { position: relative; width: 900px; height: 1200px; }
  .card {
    position: absolute; left: 80px; width: 742px; height: 442px;
    border-radius: 28px;
    background: linear-gradient(160deg, #2c2c2c 0%, var(--card) 55%, var(--card-edge) 100%);
    box-shadow: 0 6px 18px rgba(0,0,0,0.35);
    overflow: hidden;
  }
  .card--front { top: 130px; }
  .card--back { top: 638px; }

  .brand { position: absolute; display: flex; align-items: center; gap: 18px; }
  .brand__mark { background: var(--green); flex: none; }
  .brand__name {
    color: var(--white); font-weight: 600; text-transform: uppercase;
    line-height: 1.05; letter-spacing: 0.04em;
  }
  .brand__name span { display: block; }

  .card--front .brand { left: 36px; top: 50px; }
  .card--front .brand__mark { width: 52px; height: 52px; }
  .card--front .brand__name { font-size: 40px; }
  .card--front .brand__name .brand__sub { font-size: 22px; letter-spacing: 0.16em; margin-top: 6px; }

  .card--back .brand { left: 0; right: 0; top: 168px; justify-content: center; gap: 24px; }
  .card--back .brand__mark { width: 74px; height: 74px; }
  .card--back .brand__name { font-size: 56px; }
  .card--back .brand__name .brand__sub { font-size: 29px; letter-spacing: 0.17em; margin-top: 8px; }

  .person { position: absolute; left: 34px; top: 272px; }
  .person__name { color: var(--green); font-size: 26px; font-weight: 600; }
  .person__title { color: var(--soft-white); font-size: 16px; font-weight: 500; margin-top: 2px; }

  .divider {
    position: absolute; left: 34px; top: 331px; width: 649px; height: 2px;
    background: var(--green);
  }

  .contact { position: absolute; left: 36px; top: 344px; list-style: none; }
  .contact li {
    display: flex; align-items: center; gap: 12px;
    color: var(--white); font-size: 15.5px; height: 25px;
  }
  .contact svg { width: 14px; height: 14px; fill: var(--green); flex: none; }

  .licence {
    position: absolute; right: 56px; top: 388px;
    color: var(--white); font-size: 16px; font-weight: 600;
  }
  .licence__label { color: var(--green); }
</style>
</head>
<body>
<main class="canvas">

  <section class="card card--front" aria-label="Card front">
    <div class="brand">
      <div class="brand__mark"></div>
      <div class="brand__name"><span>Whitcombe</span><span class="brand__sub">Framing Works</span></div>
    </div>

    <div class="person">
      <h1 class="person__name">Marcus Pellow</h1>
      <p class="person__title">Project Manager</p>
    </div>

    <div class="divider"></div>

    <ul class="contact">
      <li>
        <svg viewBox="0 0 24 24" aria-hidden="true"><path d="M12 2a7 7 0 0 0-7 7c0 5.2 7 13 7 13s7-7.8 7-13a7 7 0 0 0-7-7zm0 9.5A2.5 2.5 0 1 1 12 6.5a2.5 2.5 0 0 1 0 5z"/></svg>
        418 Juniper Ln, Felton, CA 95092
      </li>
      <li>
        <svg viewBox="0 0 24 24" aria-hidden="true"><path d="M3 8c0-2 2-3 9-3s9 1 9 3v2h-4V8.5c-1-.4-3-.5-5-.5s-4 .1-5 .5V10H3zm3 3h12l2 8H4zm6 2a2.5 2.5 0 1 0 0 5 2.5 2.5 0 0 0 0-5z"/></svg>
        831.555.0147
      </li>
      <li>
        <svg viewBox="0 0 24 24" aria-hidden="true"><path d="M2 5h20v2l-10 6L2 7zm0 4.3l10 6 10-6V19H2z"/></svg>
        whitcombeframingworks@mailbarn.net
      </li>
    </ul>

    <p class="licence"><span class="licence__label">Lic</span> #2046318</p>
  </section>

  <section class="card card--back" aria-label="Card back">
    <div class="brand">
      <div class="brand__mark"></div>
      <div class="brand__name"><span>Whitcombe</span><span class="brand__sub">Framing Works</span></div>
    </div>
  </section>

</main>
</body>
</html>
```